Building Asset Management and Engineering Services for complex buildings

We provide asset management, project management, and engineering services for complex buildings.
Asset management services include, asset management strategies, plans, risk and conditioning assessments.
The engineering services include building services redesign, project management and commissioning services.

Target Market(s)

architects, government, electrical contractors

Industry/Entity Type

Asset Management

Contact Information for Business Card

TKB van Lorrim CPEng, FQRZolt, KTBL, VLMZ
Director
Other details such as address please refer to attached file

Font styles to use
Sans Serif

Requirements
Must have
• Fellow and Engineers logo on the back
• * Strategic Planning
• * Design
• * Documentation
• * Project Management
• * Commissioning
• * Assessment/Review
• Must have Engineers logo and wording on the back as well
Nice to have
• Good use of all the logo colours

```html
<!DOCTYPE html>
<html lang="en">
<head>
<meta charset="utf-8">
<title>Orvane Consultants – Business Card</title>
<link href="https://fonts.googleapis.com/css2?family=Michroma&display=swap" rel="stylesheet">
<style>
  :root {
    --page-bg: #e7e4df;
    --card-white: #ffffff;
    --card-grey: #f1f1f1;
    --edge-blue: #2b5c98;
    --edge-blue-dark: #1d4379;
    --back-blue-light: #3a73b3;
    --back-blue-dark: #173a6e;
    --brand-blue: #3f86c6;
    --band-red: #e01414;
    --band-red-dark: #b50707;
    --icon-red: #d81414;
    --ink: #2b2b2b;
    --white: #ffffff;
  }
  * { margin: 0; padding: 0; box-sizing: border-box; }
  html, body {
    width: 1200px; height: 1019px; overflow: hidden;
    background: var(--page-bg);
    font-family: "Michroma", sans-serif;
  }
  .card {
    position: absolute; top: 150px;
    width: 440px; height: 720px;
    box-shadow: 0 10px 30px rgba(0,0,0,.18);
    overflow: hidden;
  }
  .card--front {
    left: 130px;
    background: linear-gradient(180deg, var(--card-white) 0%, var(--card-grey) 100%);
  }
  .card--back {
    left: 630px;
    background: linear-gradient(160deg, var(--back-blue-light) 0%, var(--back-blue-dark) 100%);
    color: var(--white);
  }
  .edge {
    position: absolute; top: 0; bottom: 0; width: 24px;
    background: linear-gradient(180deg, var(--edge-blue) 0%, var(--edge-blue-dark) 100%);
  }
  .edge--left { left: 0; }
  .edge--right { right: 0; }
  .brand {
    position: absolute; top: 130px; left: 0; right: 0;
    display: flex; flex-direction: column; align-items: center;
  }
  .brand__row { display: flex; align-items: center; gap: 12px; }
  .brand__mark { width: 28px; height: 28px; background: var(--brand-blue); }
  .brand__name { font-size: 38px; color: var(--brand-blue); letter-spacing: 1px; line-height: 1; }
  .brand__sub { margin-top: 9px; font-size: 9px; color: var(--brand-blue); letter-spacing: 1px; }
  .name-band {
    position: absolute; left: 0; right: 0; top: 280px; height: 110px;
    background: linear-gradient(180deg, var(--band-red) 0%, var(--band-red-dark) 100%);
    color: var(--white); text-align: center;
    display: flex; flex-direction: column; justify-content: center; gap: 7px;
  }
  .name-band__name { font-size: 22px; font-weight: 400; letter-spacing: 2px; }
  .name-band__credentials { font-size: 11px; letter-spacing: 1px; }
  .name-band__title { font-size: 16px; letter-spacing: 2px; }
  .contacts { position: absolute; left: 40px; top: 420px; list-style: none; }
  .contact {
    display: flex; align-items: center; gap: 12px;
    height: 44px; font-size: 11px; color: var(--ink); white-space: nowrap;
  }
  .contact__icon {
    width: 28px; height: 28px; border-radius: 5px; background: var(--icon-red);
    display: flex; align-items: center; justify-content: center; flex: none;
  }
  .contact__icon svg { width: 17px; height: 17px; }
  .back__brand {
    position: absolute; top: 80px; left: 0; right: 0;
    display: flex; justify-content: center; align-items: center; gap: 12px;
  }
  .back__mark { width: 24px; height: 24px; background: var(--white); }
  .back__name { font-size: 32px; letter-spacing: 1px; line-height: 1; }
  .back__rule {
    position: absolute; top: 150px; left: 60px; right: 60px; height: 4px;
    background: var(--band-red);
  }
  .services { position: absolute; top: 200px; left: 70px; list-style: none; }
  .service {
    display: flex; align-items: center; gap: 14px;
    height: 48px; font-size: 15px; letter-spacing: 1px;
  }
  .service::before {
    content: ""; width: 10px; height: 10px; background: var(--band-red); flex: none;
  }
  .badges {
    position: absolute; bottom: 70px; left: 0; right: 0;
    display: flex; justify-content: center; gap: 40px;
  }
  .badge { width: 84px; height: 84px; background: var(--white); }
  .badge--fellow { border-radius: 50%; }
</style>
</head>
<body>
  <main class="card card--front">
    <div class="edge edge--left"></div>
    <div class="edge edge--right"></div>

    <header class="brand">
      <div class="brand__row">
        <span class="brand__mark"></span>
        <span class="brand__name">ORVANE</span>
      </div>
      <span class="brand__sub">CONSULTANTS VIC PTY LTD</span>
    </header>

    <section class="name-band">
      <h1 class="name-band__name">TKB VAN LORRIM</h1>
      <p class="name-band__credentials">CPEng, FQRZolt, KTBL, VLMZ</p>
      <p class="name-band__title">DIRECTOR</p>
    </section>

    <ul class="contacts">
      <li class="contact">
        <span class="contact__icon"><svg viewBox="0 0 20 20"><path fill="#fff" d="M5 2l3 3-1.5 2.5c1 2 2.5 3.5 4.5 4.5L13.5 10.5l3 3-2 3C8 16 4 12 3.5 4.5z"/></svg></span>
        <span>013 246 5780</span>
      </li>
      <li class="contact">
        <span class="contact__icon"><svg viewBox="0 0 20 20"><rect x="6" y="2" width="8" height="16" rx="1.5" fill="none" stroke="#fff" stroke-width="1.6"/><circle cx="10" cy="15.5" r="1" fill="#fff"/></svg></span>
        <span>013 246 5780</span>
      </li>
      <li class="contact">
        <span class="contact__icon"><svg viewBox="0 0 20 20"><rect x="3" y="8" width="14" height="9" rx="1" fill="#fff"/><rect x="6" y="3" width="8" height="6" fill="none" stroke="#fff" stroke-width="1.5"/></svg></span>
        <span>013 246 5780</span>
      </li>
      <li class="contact">
        <span class="contact__icon"><svg viewBox="0 0 20 20"><rect x="2.5" y="5" width="15" height="10" fill="#fff"/><path d="M2.5 5l7.5 6 7.5-6" fill="none" stroke="#d81414" stroke-width="1.4"/></svg></span>
        <span>hello@orvane.com</span>
      </li>
      <li class="contact">
        <span class="contact__icon"><svg viewBox="0 0 20 20" fill="none" stroke="#fff" stroke-width="1.4"><circle cx="10" cy="10" r="7"/><ellipse cx="10" cy="10" rx="3" ry="7"/><path d="M3 10h14M4.5 6h11M4.5 14h11"/></svg></span>
        <span>www.orvaneconsult.com</span>
      </li>
      <li class="contact">
        <span class="contact__icon"><svg viewBox="0 0 20 20"><path fill="#fff" d="M10 2a5.5 5.5 0 0 0-5.5 5.5C4.5 12 10 18 10 18s5.5-6 5.5-10.5A5.5 5.5 0 0 0 10 2z"/><circle cx="10" cy="7.5" r="2" fill="#d81414"/></svg></span>
        <span>071,12th floor,Harbour Quay Road KTB</span>
      </li>
    </ul>
  </main>

  <section class="card card--back">
    <div class="back__brand">
      <span class="back__mark"></span>
      <span class="back__name">ORVANE</span>
    </div>
    <div class="back__rule"></div>
    <ul class="services">
      <li class="service">Strategic Planning</li>
      <li class="service">Design</li>
      <li class="service">Documentation</li>
      <li class="service">Project Management</li>
      <li class="service">Commissioning</li>
      <li class="service">Assessment/Review</li>
    </ul>
    <div class="badges">
      <span class="badge badge--fellow" role="img" aria-label="Fellow membership badge"></span>
      <span class="badge badge--engineers" role="img" aria-label="Engineers membership badge"></span>
    </div>
  </section>
</body>
</html>
```